Harvesting Victors 6x9 book soft cover- front cover only

We need a book cover for a softcover book. We will need final files in Photoshop or InDesign is preferred.

Overall Title:
Harvesting Victors
Subtitle:
The Foundations of Humble Mentoring for Trainers, Instructors and Players
Author:
by Dr. Marcus Pettiford

The audience is high school and college coaches however we don't want the standard picture with words over the top. Make it a creative design but keep it mind it's a little academic.

```html
<!DOCTYPE html>
<html lang="en">
<head>
<meta charset="utf-8">
<title>Harvesting Victors — Front Cover</title>
<link rel="stylesheet" href="https://fonts.googleapis.com/css2?family=Anton&family=Oswald:wght@400;500&display=swap">
<style>
  :root {
    --backdrop: #050505;
    --band-red: #c8161a;
    --title-red: #d10a0a;
    --navy: #1b2858;
    --cream-light: #f8f5f2;
    --cream-dark: #efe8e2;
    --white: #ffffff;
  }
  html, body {
    margin: 0;
    padding: 0;
    width: 1200px;
    height: 2400px;
    overflow: hidden;
    background: var(--backdrop);
  }
  .canvas {
    position: relative;
    width: 1200px;
    height: 2400px;
    background: var(--backdrop);
  }
  .book-cover {
    position: absolute;
    left: 151px;
    top: 526px;
    width: 899px;
    height: 1347px;
    display: block;
  }
  .subtitle {
    font-family: "Oswald", "Arial Narrow", sans-serif;
    font-weight: 500;
    font-size: 47px;
    fill: var(--white);
  }
  .author {
    font-family: "Oswald", "Arial Narrow", sans-serif;
    font-weight: 500;
    font-size: 60px;
    fill: var(--white);
  }
  .title-lead {
    font-family: "Anton", "Impact", sans-serif;
    font-size: 146px;
    fill: var(--navy);
  }
  .title-main {
    font-family: "Anton", "Impact", sans-serif;
    font-size: 320px;
    fill: var(--title-red);
  }
</style>
</head>
<body>
<main class="canvas">
  <svg class="book-cover" viewBox="0 0 899 1347" xmlns="http://www.w3.org/2000/svg" aria-label="Harvesting Victors book cover">
    <defs>
      <linearGradient id="paper" x1="0" y1="0" x2="1" y2="1">
        <stop offset="0" stop-color="var(--cream-light)"/>
        <stop offset="1" stop-color="var(--cream-dark)"/>
      </linearGradient>
    </defs>

    <rect class="paper-field" width="899" height="1347" fill="url(#paper)"/>

    <path class="top-band" fill="var(--band-red)"
      d="M0 0 H899 V270 L862 273 L818 271 L790 273 L760 281 L742 286 L712 282 L690 280 L652 276 L612 271 L578 270 L556 266 L522 259 L488 249 L452 244 L420 244 L390 240 L352 232 L318 229 L290 231 L272 238 L262 246 L270 252 L258 258 L236 262 L214 268 L196 272 L170 272 L150 276 L118 279 L90 276 L66 280 L42 277 L20 284 L0 286 Z"/>

    <text class="subtitle" x="449.5" y="123" text-anchor="middle" textLength="615" lengthAdjust="spacingAndGlyphs">THE FOUNDATIONS OF HUMBLE MENTORING FOR</text>
    <text class="subtitle" x="449.5" y="168" text-anchor="middle" textLength="500" lengthAdjust="spacingAndGlyphs">TRAINERS, INSTRUCTORS AND PLAYERS</text>

    <text class="title-lead" x="449.5" y="449" text-anchor="middle" textLength="664" lengthAdjust="spacingAndGlyphs">HARVESTING</text>
    <text class="title-main" x="449.5" y="748" text-anchor="middle" textLength="520" lengthAdjust="spacing">VIC</text>
    <text class="title-main" x="449.5" y="1053" text-anchor="middle" textLength="673" lengthAdjust="spacingAndGlyphs">TORS</text>

    <path class="bottom-band" fill="var(--navy)"
      d="M0 1119 L40 1118 L92 1114 L140 1112 L176 1110 L208 1108 L224 1100 L216 1094 L232 1090 L272 1092 L318 1096 L360 1100 L402 1104 L448 1104 L500 1100 L546 1102 L590 1108 L640 1108 L690 1104 L736 1101 L746 1095 L774 1093 L806 1094 L836 1091 L862 1088 L880 1094 L899 1092 V1347 H0 Z"/>

    <text class="author" x="449.5" y="1270" text-anchor="middle" textLength="652" lengthAdjust="spacing">BY DR. MARCUS PETTIFORD</text>
  </svg>
</main>
</body>
</html>
```